Two Rollup Banners Promoting Trade Association

UPDATE: Please do not recycle the prior designs we've had. I am looking for creativity and a new look. Otherwise, I would use the prior designers to just update their work.
I need two 48"x79" Pull Up Retractable Banners Designed.
One promotes the benefits of membership in the Residential Capital Partners Forum. The second promotes RCPF's role in the affordable housing ecosystem.
The content for each is attached. I'm also providing examples of two banners we recently created for our 30th Anniversary as well as some photos of our members if you choose to use them (although it's not necessary - just providing them as an option).
The banners don't have to mimic the ones we did for our 30th Anniversary. I'm simply providing them as examples of designs that meet the look and feel of our brand.
I've also provided our brand guidelines and the specs for the banner.
Updates
All,
We are looking for clean, modern, streamlined designs. No clip art. No waves. Don’t bury the message in the graphics.
Please keep that in mind as you submit designs.
Look and feel
Each slider illustrates characteristics of the customer's brand and the style your logo design should communicate.

```html
<!DOCTYPE html>
<html lang="en">
<head>
<meta charset="utf-8">
<title>RCPF Rollup Banners</title>
<link rel="stylesheet" href="https://fonts.googleapis.com/css2?family=Montserrat:wght@500;800&family=Hind:wght@500;600;700&family=Bungee&display=swap">
<style>
  :root {
    --orange: #F47629;
    --coral: #F06C4B;
    --deep-orange: #E85A20;
    --yellow: #F5B41A;
    --soft-yellow: #F7C546;
    --ink: #4A4D52;
    --blue: #1E3FB0;
    --black: #111111;
    --white: #FFFFFF;
    --stage: #E6E7E9;
  }
  * { margin: 0; padding: 0; box-sizing: border-box; }
  html, body { width: 1067px; height: 1200px; overflow: hidden; background: var(--stage); }
  .stage { position: relative; width: 1067px; height: 1200px; }
  .banner {
    position: absolute; top: 160px; width: 500px; height: 880px;
    background: var(--white); overflow: hidden;
    font-family: "Hind", sans-serif;
    box-shadow: 0 6px 18px rgba(0,0,0,.12);
  }
  .banner--members { left: 20px; }
  .banner--ecosystem { left: 547px; }
  .banner__art { position: absolute; inset: 0; width: 500px; height: 880px; }
  .brand {
    position: absolute; top: 50px; left: 0; width: 100%;
    display: flex; justify-content: center; align-items: center; gap: 10px;
  }
  .brand__dot { width: 34px; height: 34px; border-radius: 50%; background: var(--orange); }
  .brand__name { font-family: "Hind", sans-serif; font-weight: 700; font-size: 46px; line-height: 1; color: var(--ink); padding-top: 6px; }
  .headline { position: absolute; font-family: "Montserrat", sans-serif; line-height: 1; white-space: nowrap; }
  .headline__accent { color: var(--orange); font-weight: 800; }
  .headline__plain { color: var(--ink); font-weight: 500; display: block; }
  .banner--members .headline { left: 52px; top: 120px; font-size: 38px; }
  .banner--members .headline__plain { margin-top: 12px; font-size: 40px; }
  .banner--ecosystem .headline { left: 51px; top: 130px; font-size: 32px; }
  .banner--ecosystem .headline__plain { margin-top: 12px; font-size: 31px; font-weight: 700; }
  .pill-tag {
    position: absolute; left: 52px; top: 223px; width: 201px; height: 33px;
    border-radius: 17px; background: var(--orange); color: var(--white);
    font-weight: 700; font-size: 16px; display: flex; align-items: center; justify-content: center; padding-top: 3px;
  }
  .benefits { position: absolute; left: 52px; top: 274px; list-style: none; }
  .benefits li { display: flex; align-items: center; gap: 14px; height: 30px; margin-bottom: 7px; font-size: 17.5px; font-weight: 600; color: var(--ink); line-height: 1.05; }
  .benefits li.benefits__tall { height: 40px; }
  .benefits b { color: var(--blue); font-weight: 600; }
  .benefits svg { flex: none; width: 30px; height: 30px; }
  .roles { position: absolute; left: 50px; top: 243px; list-style: none; }
  .roles li { display: flex; align-items: center; gap: 12px; height: 28px; margin-bottom: 8.5px; font-size: 15.5px; font-weight: 700; color: var(--blue); }
  .roles svg { flex: none; width: 24px; height: 26px; }
  .outline-tag {
    position: absolute; height: 28px; border-radius: 14px; border: 1.5px solid;
    font-weight: 600; font-size: 15px; letter-spacing: .3px;
    display: flex; align-items: center; justify-content: center; padding-top: 3px;
  }
  .banner--members .outline-tag { left: 46px; top: 645px; width: 148px; color: var(--white); border-color: var(--white); }
  .banner--ecosystem .outline-tag { left: 244px; top: 461px; width: 148px; color: var(--black); border-color: var(--black); }
  .facts { position: absolute; color: var(--white); font-size: 15.5px; font-weight: 500; line-height: 20.5px; }
  .banner--members .facts { left: 46px; top: 683px; }
  .banner--ecosystem .facts--standards { left: 242px; top: 500px; }
  .banner--ecosystem .facts--impact { left: 242px; top: 606px; }
  .join {
    position: absolute; width: 127px; height: 30px; border-radius: 15px; background: var(--black);
    color: var(--soft-yellow); font-family: "Bungee", sans-serif; font-size: 12px;
    display: flex; align-items: center; justify-content: center;
  }
  .banner--members .join { left: 45px; top: 776px; }
  .banner--ecosystem .join { left: 241px; top: 697px; }
  .web { position: absolute; display: flex; align-items: center; gap: 8px; color: var(--white); font-family: "Montserrat", sans-serif; font-weight: 500; font-size: 18px; }
  .web svg { width: 26px; height: 26px; }
  .banner--members .web { left: 45px; top: 815px; }
  .banner--ecosystem .web { left: 241px; top: 737px; }
</style>
</head>
<body>
<main class="stage">

  <!-- Membership banner -->
  <section class="banner banner--members">
    <svg class="banner__art" viewBox="0 0 500 880" aria-hidden="false">
      <defs>
        <linearGradient id="photoToneA" x1="0" y1="0" x2="1" y2="1">
          <stop offset="0" stop-color="#E9E6E1"/>
          <stop offset=".55" stop-color="#8E8A86"/>
          <stop offset="1" stop-color="#3B4656"/>
        </linearGradient>
        <linearGradient id="baseFadeA" x1="0" y1="0" x2="0" y2="1">
          <stop offset="0" stop-color="#F06C4B" stop-opacity="0"/>
          <stop offset="1" stop-color="#E06A1E" stop-opacity=".55"/>
        </linearGradient>
      </defs>
      <circle cx="560" cy="-70" r="185" fill="var(--soft-yellow)"/>
      <path d="M0,438 Q250,620 500,620 L500,880 L0,880 Z" fill="var(--coral)"/>
      <circle cx="432" cy="672" r="228" fill="var(--yellow)"/>
      <g role="img" aria-label="Photo of two members talking at a conference">
        <circle cx="432" cy="672" r="221" fill="url(#photoToneA)"/>
      </g>
      <path d="M0,438 Q250,620 500,620 L500,880 L0,880 Z" fill="var(--coral)" opacity=".85"/>
      <circle cx="166" cy="812" r="196" fill="var(--yellow)" opacity=".55"/>
      <rect x="0" y="560" width="500" height="320" fill="url(#baseFadeA)"/>
    </svg>

    <div class="brand"><span class="brand__dot"></span><span class="brand__name">RCPF</span></div>

    <h1 class="headline"><span class="headline__accent">LIHTC INVESTOR-</span><span class="headline__plain">ONLY COMMUNITY</span></h1>

    <div class="pill-tag">WHERE INVESTORS</div>

    <ul class="benefits">
      <li><svg viewBox="0 0 30 30"><circle cx="15" cy="15" r="15" fill="var(--orange)"/><circle cx="15" cy="15" r="4" fill="none" stroke="#fff" stroke-width="1.6"/><path d="M15 6v5M15 19v5M6 15h5M19 15h5" stroke="#fff" stroke-width="1.6"/></svg><span><b>NETWORK:</b> Peer Groups &amp; Forums</span></li>
      <li><svg viewBox="0 0 30 30"><circle cx="15" cy="15" r="15" fill="var(--orange)"/><rect x="9" y="8" width="12" height="9" fill="none" stroke="#fff" stroke-width="1.6"/><circle cx="15" cy="21" r="2" fill="#fff"/></svg><span><b>LEARN:</b> Conferences &amp; Webinars</span></li>
      <li><svg viewBox="0 0 30 30"><circle cx="15" cy="15" r="15" fill="var(--orange)"/><circle cx="11" cy="11" r="2.5" fill="#fff"/><circle cx="20" cy="19" r="2.5" fill="#fff"/><path d="M11 15v7M13 12l5 5" stroke="#fff" stroke-width="1.6"/></svg><span><b>SHARE:</b> Candid Investor-Only Exchange</span></li>
      <li><svg viewBox="0 0 30 30"><circle cx="15" cy="15" r="15" fill="var(--orange)"/><circle cx="15" cy="15" r="7" fill="none" stroke="#fff" stroke-width="1.8"/><path d="M9 15h12" stroke="#fff" stroke-width="1.8"/></svg><span><b>SHAPE:</b> Industry Standards &amp; Best Practices</span></li>
      <li class="benefits__tall"><svg viewBox="0 0 30 30"><circle cx="15" cy="15" r="15" fill="var(--orange)"/><path d="M9 21l5-5 3 3 5-7" fill="none" stroke="#fff" stroke-width="1.8"/></svg><span><b>GROW:</b> Professional Development &amp;<br>Emerging Leaders Program</span></li>
    </ul>

    <div class="outline-tag">OUR COMMUNITY</div>
    <p class="facts">60+ Investor Firms &nbsp; 1,000+ Industry<br>Professionals Banks (Large &amp; Small), Insurance<br>Companies, Economic Investors</p>

    <div class="join">JOIN US TODAY</div>
    <div class="web"><svg viewBox="0 0 26 26"><circle cx="13" cy="13" r="12" fill="#fff" opacity=".9"/><g fill="none" stroke="var(--orange)" stroke-width="1.3"><circle cx="13" cy="13" r="7.5"/><ellipse cx="13" cy="13" rx="3.2" ry="7.5"/><path d="M5.5 13h15M7 9h12M7 17h12"/></g></svg>www.rcpf-forum.org</div>
  </section>

  <!-- Ecosystem banner -->
  <section class="banner banner--ecosystem">
    <svg class="banner__art" viewBox="0 0 500 880">
      <defs>
        <linearGradient id="photoToneB" x1="0" y1="0" x2="1" y2="1">
          <stop offset="0" stop-color="#6E655E"/>
          <stop offset=".5" stop-color="#D9D3CB"/>
          <stop offset="1" stop-color="#8A8FB0"/>
        </linearGradient>
        <linearGradient id="baseFadeB" x1="0" y1="0" x2="0" y2="1">
          <stop offset="0" stop-color="#E85A20" stop-opacity="0"/>
          <stop offset="1" stop-color="#D0561C" stop-opacity=".5"/>
        </linearGradient>
      </defs>
      <circle cx="560" cy="-70" r="190" fill="var(--soft-yellow)"/>
      <path d="M0,434 Q220,610 500,620 L500,880 L0,880 Z" fill="var(--coral)"/>
      <circle cx="470" cy="870" r="475" fill="var(--yellow)"/>
      <circle cx="419" cy="952" r="294" fill="var(--deep-orange)"/>
      <rect x="0" y="600" width="500" height="280" fill="url(#baseFadeB)"/>
      <circle cx="90" cy="805" r="132" fill="var(--yellow)"/>
      <g role="img" aria-label="Photo of members in conversation at a conference table">
        <circle cx="84" cy="810" r="126" fill="url(#photoToneB)"/>
      </g>
    </svg>

    <div class="brand"><span class="brand__dot"></span><span class="brand__name">RCPF</span></div>

    <h1 class="headline"><span class="headline__accent">WHERE LIHTC INVESTING</span><span class="headline__plain">EXCELLENCE BEGINS</span></h1>

    <ul class="roles">
      <li><svg viewBox="0 0 24 26"><path d="M2 24L11 2h4L6 24z" fill="var(--orange)"/><path d="M9 24L18 2h4L13 24z" fill="var(--ink)"/></svg>Setting Industry Standards &amp; Best Practices</li>
      <li><svg viewBox="0 0 24 26"><path d="M2 24L11 2h4L6 24z" fill="var(--orange)"/><path d="M9 24L18 2h4L13 24z" fill="var(--ink)"/></svg>Building Community Through Candid Exchange</li>
      <li><svg viewBox="0 0 24 26"><path d="M2 24L11 2h4L6 24z" fill="var(--orange)"/><path d="M9 24L18 2h4L13 24z" fill="var(--ink)"/></svg>Promoting the Investor Perspective</li>
      <li><svg viewBox="0 0 24 26"><path d="M2 24L11 2h4L6 24z" fill="var(--orange)"/><path d="M9 24L18 2h4L13 24z" fill="var(--ink)"/></svg>Fostering Collaboration Across the Ecosystem</li>
    </ul>

    <div class="outline-tag">OUR COMMUNITY</div>
    <p class="facts facts--standards">Industry-Adopted Standards in<br>Underwriting, Asset Management,<br>Risk Rating &amp; More</p>
    <p class="facts facts--impact">4 Million Rental Homes Created<br>9.28 Million Low-Income<br>Households Served</p>

    <div class="join">JOIN US TODAY</div>
    <div class="web"><svg viewBox="0 0 26 26"><circle cx="13" cy="13" r="12" fill="#fff" opacity=".9"/><g fill="none" stroke="var(--orange)" stroke-width="1.3"><circle cx="13" cy="13" r="7.5"/><ellipse cx="13" cy="13" rx="3.2" ry="7.5"/><path d="M5.5 13h15M7 9h12M7 17h12"/></g></svg>www.rcpf-forum.org</div>
  </section>

</main>
</body>
</html>
```